Business card for law firm

Need business card for new law firm. Think confident, authoritative, conservative, but not stuffy or old-fashioned.

Contact Information for Business Card

Content for card - logo (uploaded), plus the following:

Paul Wexbury (larger font)
Managing Partner (larger font, but not as large as name)
Level 9, 41 Tansy Lane
Sydney NSW 2000
Main Tel 02 7346 2190
Direct Tel 02 6273 4415
Email paul@qvlegal.com.au
www.qvlegal.com.au

Letterhead design should include logo plus:
Level 9, 41 Tansy Lane
Sydney NSW 2000
Tel 02 6273 4415
www.qvlegal.com.au

```html
<!DOCTYPE html>
<html lang="en">
<head>
<meta charset="utf-8">
<title>Paul Wexbury – Business Card</title>
<link href="https://fonts.googleapis.com/css2?family=Bebas+Neue&family=Arimo:wght@400;700&display=swap" rel="stylesheet">
<style>
  :root {
    --navy: #001b57;
    --white: #ffffff;
    --backdrop: #f2f2f2;
    --shadow: rgba(0, 0, 0, 0.18);
  }
  * { margin: 0; padding: 0; box-sizing: border-box; }
  html, body {
    width: 1200px;
    height: 1200px;
    overflow: hidden;
    background: var(--backdrop);
  }
  .canvas {
    position: relative;
    width: 1200px;
    height: 1200px;
  }
  .business-card {
    position: absolute;
    left: 320px;
    top: 110px;
    width: 560px;
    height: 981px;
    background: var(--navy);
    box-shadow: 0 10px 30px var(--shadow);
    color: var(--white);
    text-align: center;
  }
  .card-name {
    position: absolute;
    top: 72px;
    left: 0;
    width: 100%;
    font-family: "Bebas Neue", "Arial Narrow", sans-serif;
    font-weight: 400;
    font-size: 89px;
    line-height: 1;
    letter-spacing: 0.5px;
  }
  .card-title {
    position: absolute;
    top: 172px;
    left: 0;
    width: 100%;
    font-family: "Bebas Neue", "Arial Narrow", sans-serif;
    font-size: 36px;
    line-height: 1;
  }
  .card-contact {
    position: absolute;
    top: 410px;
    left: 0;
    width: 100%;
    font-family: Arimo, Arial, sans-serif;
    font-weight: 700;
    font-size: 30px;
    line-height: 40px;
  }
  .contact-group + .contact-group { margin-top: 38px; }
  .card-footer {
    position: absolute;
    left: 0;
    bottom: 0;
    width: 100%;
    height: 171px;
    background: var(--white);
    display: flex;
    flex-direction: column;
    align-items: center;
    justify-content: center;
    gap: 16px;
  }
  .firm-square {
    width: 38px;
    height: 38px;
    background: var(--navy);
  }
  .firm-name {
    font-family: Arimo, Arial, sans-serif;
    font-weight: 400;
    font-size: 24px;
    letter-spacing: 2px;
    color: var(--navy);
  }
</style>
</head>
<body>
  <main class="canvas">
    <article class="business-card">
      <h1 class="card-name">PAUL WEXBURY</h1>
      <p class="card-title">MANAGING PARTNER</p>
      <div class="card-contact">
        <p class="contact-group">Level 9, 41 Tansy Lane<br>Sydney NSW 2000</p>
        <p class="contact-group">Tel: 02 7346 2190<br>Tel: 02 6273 4415</p>
        <p class="contact-group">Email paul@qvlegal.com.au<br>www.qvlegal.com.au</p>
      </div>
      <footer class="card-footer">
        <span class="firm-square"></span>
        <span class="firm-name">WEXBURY LAWYERS</span>
      </footer>
    </article>
  </main>
</body>
</html>
```